Need a Crisps (Potato Chips in US) and Popcorns Logo, Artwork and Packaging Design

I want to package my home made crisps and popcorns. The crisps will be going by the name ZapZoz (Ks are capital) and the popcorns by the name bumbim (Should all be in same case, either all small or all caps - I leave it to designer's choice).

Crisps:
I want both a logo that will be associated with the product and a package design with the logo embedded. The logo should be playful and striking.

The packaging for the crisps should be to the standards of international brands like Vorn, Flumbix, Garvelo, etc. Package type is the pouch based packages.

The colours should be vibrant. We are limited to 4 colours in the design due to printing costs. So the designer should use a mixture that is striking especially to children and young adults.

Incorporation of animal artwork is allowed as long as it does not infringe on IPs.

Popcorns:
This one is less intensive and only requires a logo and package design like the one used in movie halls.

Target Market(s)

Kids and young adults

Industry/Entity Type

Food Production

Logo Text

ZapZoz for crisps and bumbim for popcorn

Colors

Designer to choose colors to be used in the design.

Requirements
Must have
• Playful font and colours
Nice to have
• Distinguishing artwork

```html
<!DOCTYPE html>
<html lang="en">
<head>
<meta charset="utf-8">
<title>bumbim Popcorn Pack</title>
<link href="https://fonts.googleapis.com/css2?family=Arimo:wght@700&family=Michroma&display=swap" rel="stylesheet">
<style>
  :root {
    --red: #e3200f;
    --deep-red: #a80f08;
    --orange: #f26a12;
    --amber: #f7a21a;
    --yellow: #fbd31c;
    --gold: #e09a10;
    --navy: #1a1f7a;
    --white: #ffffff;
    --popcorn-light: #f3ead8;
    --popcorn-shade: #c9a46a;
  }
  html, body {
    margin: 0;
    padding: 0;
    width: 847px;
    height: 1200px;
    overflow: hidden;
    background: #ffffff;
  }
  .pack {
    display: block;
    width: 847px;
    height: 1200px;
  }
  .brand-name {
    font-family: "Arimo", sans-serif;
    font-weight: 700;
    font-size: 62px;
    fill: var(--deep-red);
  }
  .product-name {
    font-family: "Michroma", sans-serif;
    font-size: 56px;
    fill: var(--white);
    letter-spacing: 1px;
  }
  .net-weight {
    font-family: "Arimo", sans-serif;
    font-weight: 700;
    font-size: 20px;
    fill: var(--white);
  }
</style>
</head>
<body>
<svg class="pack" viewBox="0 0 638 903" preserveAspectRatio="none" xmlns="http://www.w3.org/2000/svg">
  <defs>
    <linearGradient id="bg-warm" x1="0" y1="0" x2="1" y2="1">
      <stop offset="0" stop-color="var(--red)"/>
      <stop offset="0.45" stop-color="var(--orange)"/>
      <stop offset="1" stop-color="var(--yellow)"/>
    </linearGradient>
    <linearGradient id="band-red" x1="0" y1="0" x2="1" y2="0">
      <stop offset="0" stop-color="var(--deep-red)"/>
      <stop offset="1" stop-color="var(--red)"/>
    </linearGradient>
    <linearGradient id="band-yellow" x1="0" y1="0" x2="1" y2="0">
      <stop offset="0" stop-color="var(--amber)"/>
      <stop offset="1" stop-color="var(--yellow)"/>
    </linearGradient>
    <linearGradient id="shield-frame" x1="0" y1="0" x2="1" y2="1">
      <stop offset="0" stop-color="var(--yellow)"/>
      <stop offset="0.5" stop-color="var(--gold)"/>
      <stop offset="1" stop-color="var(--orange)"/>
    </linearGradient>
    <linearGradient id="shield-fill" x1="0" y1="0" x2="0" y2="1">
      <stop offset="0" stop-color="#f2d56a"/>
      <stop offset="0.6" stop-color="var(--gold)"/>
      <stop offset="1" stop-color="#c97a0c"/>
    </linearGradient>
    <radialGradient id="popcorn-tone" cx="0.5" cy="0.4" r="0.6">
      <stop offset="0" stop-color="var(--popcorn-light)"/>
      <stop offset="1" stop-color="var(--popcorn-shade)"/>
    </radialGradient>
  </defs>

  <!-- background -->
  <rect class="backdrop" width="638" height="903" fill="url(#bg-warm)"/>

  <!-- top-right stripes -->
  <g class="top-stripes">
    <polygon points="150,0 638,0 638,205 470,130" fill="var(--red)"/>
    <polygon points="215,0 290,0 638,150 638,185" fill="var(--yellow)" opacity="0.85"/>
    <polygon points="330,0 638,0 638,100" fill="var(--deep-red)"/>
  </g>

  <!-- popcorn photo area -->
  <path class="popcorn-photo" role="img" aria-label="Photo of a bucket heaped with fresh popcorn"
        d="M96,190 Q120,110 230,95 Q320,70 420,95 Q540,120 560,200 L560,330 L96,330 Z"
        fill="url(#popcorn-tone)"/>

  <!-- shield -->
  <g class="shield">
    <polygon points="78,205 320,320 578,205 578,500 320,640 78,500"
             fill="url(#shield-frame)"/>
    <polygon points="100,225 320,330 560,225 560,490 320,620 100,490"
             fill="url(#shield-fill)" opacity="0.9"/>
    <polygon points="96,208 320,318 575,212 575,232 320,340 96,228" fill="var(--red)"/>
    <polyline points="130,250 320,340 515,250 515,490 320,590 130,490 130,250"
              fill="none" stroke="var(--navy)" stroke-width="3"/>
  </g>

  <!-- brand -->
  <text class="brand-name" x="320" y="434" text-anchor="middle">bumbim</text>

  <!-- bottom bands -->
  <g class="bottom-bands">
    <polygon points="0,505 638,700 638,745 0,600" fill="var(--red)"/>
    <polygon points="0,600 638,745 638,840 0,770" fill="url(#band-red)"/>
    <polygon points="0,770 638,840 638,903 0,903" fill="url(#band-yellow)"/>
  </g>

  <!-- product name -->
  <text class="product-name" x="100" y="720" transform="rotate(9 100 720)">POPCORN</text>

  <!-- net weight -->
  <g class="weight-badge">
    <rect x="36" y="833" width="76" height="37" fill="var(--navy)"/>
    <text class="net-weight" x="74" y="859" text-anchor="middle">180g</text>
  </g>
</svg>
</body>
</html>
```